Web Design for historic veg friendly, organic restaurant

We need a new web site. The Brookmere Cafe is a 40 year old restaurant in Chicago. We've been one of the premier, casual vegetarian restaurants since we opened. 5 years ago, Brookmere Cafe was purchased from the original owners by a local, certified organic farmer. We are nearly 100% from scratch kitchen, 100% certified organic produce, we are governed by a strict sustainable plan and we are very active politically. But you wouldn't know it form our website! We have a desire to build a simple website around some basic principles:
1. We need our current logo prominently displayed (logo attached)
2. We need a "click to call" easily accessible
3. We have an online order link that needs to be easily accessible
4. We need our hours, location, and directions easy to see
4. We need a separate events page (we have a live music and events venue that runs shows 5-7 nights per week.)
5. We would like to have a separate page for pictures, particularly old pictures. It would be fun to have a function for people to post their own shots, but that might make this too complicated. If it were possible, we would of course need to retain the ability to curate posted pictures.
6. This needs to be easily edited by us, so in a platform such as word press or similar
7. We will need this mobile enhanced

Target Market(s)

Neighborhood residents - zip code is 60626

Industry/Entity Type

Restaurant

Coding

Coded - Design and coding required

Number of Pages Required

4 page

Font styles to use
Sans Serif

Requirements
Must have
• Logo, click to call, events page that we can manage, contact us, about us page, menu (we have the online menu through a third party plugin), a page for our market and some nice pictures on our splash page,
• Must be mobile ready and on a platform such as Word Press or some other platform where we can edit on our own
Nice to have
• Page for past employees and historical pictures, be nice to have food pictures or something similar on a scroll, would love to have an ability for others to post pictures that we would "approve"
Should not have
• We don't need anything that spins, moves, flames or other features that detract from gathering information

```html
<!DOCTYPE html>
<html lang="en">
<head>
<meta charset="utf-8">
<title>The Brookmere Cafe</title>
<link href="https://fonts.googleapis.com/css2?family=Montserrat:wght@400;500;600;700&family=Open+Sans:wght@400;600&family=Dancing+Script:wght@500;700&display=swap" rel="stylesheet">
<style>
:root{
  --red:#e8322a;
  --red-dark:#c8231c;
  --ink:#222222;
  --text:#555555;
  --muted:#888888;
  --paper:#ffffff;
  --panel:#f4f3f2;
  --dark:#1c1b1a;
  --footer:#141414;
  --line:#dddddd;
}
*{box-sizing:border-box;margin:0;padding:0}
html,body{width:1200px;height:4317px;overflow:hidden}
body{position:relative;background:var(--paper);font-family:"Open Sans",Arial,sans-serif;color:var(--text)}
.abs{position:absolute}
.heading{font-family:"Montserrat",Arial,sans-serif;color:var(--ink);font-weight:500;text-align:center;letter-spacing:1px}
.script{font-family:"Dancing Script",cursive;color:var(--red);font-weight:700}
.underline{width:70px;height:2px;background:var(--red);margin:14px auto 0}

/* hero */
.hero{left:0;top:0;width:1200px;height:633px;background:radial-gradient(ellipse at 75% 45%,#5a4132 0%,#3a2a20 40%,#1e1712 100%)}
.hero-shade{left:0;top:0;width:1200px;height:633px;background:linear-gradient(90deg,rgba(0,0,0,.45),rgba(0,0,0,0) 60%)}
.brand{left:86px;top:30px;display:flex;align-items:center;gap:10px;font-family:"Montserrat",sans-serif;font-weight:700;font-size:24px;color:#f2c230}
.brand-dot{width:22px;height:22px;border-radius:50%;background:#f2c230}
.topbar{right:86px;top:34px;display:flex;align-items:center;gap:10px;font-family:"Montserrat",sans-serif;font-size:13px;color:#fff}
.social{width:24px;height:24px;border:1.5px solid #fff;border-radius:50%}
.topbar .cart{margin-left:14px;font-weight:600}
.nav{right:86px;top:90px;display:flex;gap:44px;font-family:"Montserrat",sans-serif;font-size:14px;color:#fff;font-weight:500}
.hero-text{left:86px;top:250px;color:#fff;font-family:"Montserrat",sans-serif}
.hero-text .small{font-size:38px;font-weight:400;letter-spacing:1px}
.hero-text .big{font-size:50px;font-weight:400;letter-spacing:1px;margin-top:6px}
.hero-text p{font-family:"Open Sans",sans-serif;font-size:14px;line-height:22px;width:520px;margin-top:26px;color:#eee}
.btn-ghost{display:inline-block;margin-top:30px;border:1.5px solid #fff;padding:14px 26px;font-size:16px;font-weight:500;color:#fff}
.dots{left:582px;top:580px;display:flex;gap:10px}
.dots i{width:9px;height:9px;border-radius:50%;background:rgba(255,255,255,.5)}
.dots i.on{background:#fff}

/* info bar */
.infobar{left:0;top:639px;width:1200px;height:103px;background:var(--red);display:flex;color:#fff;font-family:"Montserrat",sans-serif}
.info{flex:1;display:flex;align-items:center;padding-left:86px;position:relative;border-right:1px solid rgba(255,255,255,.35)}
.info:last-child{border-right:none}
.info:nth-child(2),.info:nth-child(3){padding-left:50px}
.info svg{width:44px;height:44px;margin-right:18px}
.info b{display:block;font-size:17px;font-weight:500}
.info span{font-size:14px}
.info .bubble{position:absolute;right:50px;top:37px;width:28px;height:28px;border-radius:50%;background:rgba(255,255,255,.3)}

/* about */
.about-photo{left:86px;top:758px;width:533px;height:528px;background:radial-gradient(circle at 45% 45%,#7a5a3a 0%,#4a3a30 45%,#2c2420 100%)}
.about-panel{left:639px;top:758px;width:475px;height:528px;background:var(--panel);text-align:center;padding-top:48px}
.about-panel h2{font-size:40px}
.about-panel .script{font-size:27px;margin-top:14px}
.about-panel p{font-size:12.5px;line-height:21px;width:380px;margin:22px auto 0;color:var(--text)}
.btn-red{display:inline-block;background:var(--red);color:#fff;font-family:"Montserrat",sans-serif;font-size:14px;font-weight:500;padding:13px 26px}
.about-panel .btn-red{margin-top:28px}

/* gallery */
.gallery-title{left:0;top:1335px;width:1200px}
.gallery-title h2{font-size:38px}
.ph{border:none}
.g1{left:86px;top:1430px;width:239px;height:363px;background:linear-gradient(160deg,#2e4a22,#6b5a2a 60%,#c69a3a)}
.g2{left:348px;top:1430px;width:239px;height:167px;background:linear-gradient(150deg,#1a1512,#4a3324)}
.g3{left:610px;top:1430px;width:239px;height:167px;background:linear-gradient(150deg,#3a2a1c,#b88750)}
.g4{left:875px;top:1430px;width:236px;height:363px;background:linear-gradient(170deg,#7a3a5a,#b9a48a 50%,#6a7a4a)}
.g5{left:348px;top:1620px;width:501px;height:173px;background:linear-gradient(90deg,#1b2430,#3a4652 50%,#8a6a48)}

/* share */
.share{left:0;top:1851px;width:1200px;height:103px;background:var(--red);color:#fff;font-family:"Montserrat",sans-serif}
.share h3{position:absolute;left:86px;top:22px;font-size:28px;font-weight:500}
.share p{position:absolute;left:86px;top:66px;font-size:12.5px;font-family:"Open Sans",sans-serif}
.share .share-btn{position:absolute;left:862px;top:26px;width:252px;height:52px;background:var(--red-dark);text-align:center;line-height:52px;font-size:26px;font-weight:500}

/* menu */
.menu{left:0;top:1957px;width:1200px;height:763px;background:#f6f5f3}
.menu-head{position:absolute;left:0;top:50px;width:1200px}
.menu-head h2{font-size:38px}
.menu-head p{text-align:center;font-size:12.5px;margin-top:22px;color:var(--text)}
.tabs{position:absolute;left:230px;top:184px;display:flex;gap:18px}
.tab{width:132px;height:35px;background:#fff;border:1px solid var(--line);text-align:center;line-height:33px;font-family:"Montserrat",sans-serif;font-size:12px;color:var(--ink)}
.tab.active{color:var(--red)}
.dish{position:absolute;width:498px;height:100px}
.dish .pic{position:absolute;left:0;top:0;width:144px;height:86px}
.dish h4{position:absolute;left:170px;top:-2px;font-size:22px}
.dish .price{position:absolute;right:0;top:0;font-family:"Montserrat",sans-serif;font-size:18px;font-weight:600;color:var(--ink)}
.dish p{position:absolute;left:170px;top:42px;width:320px;font-size:12.5px;line-height:19px}
.dish p em{font-style:normal;color:var(--red)}
.pic-a{background:linear-gradient(135deg,#3c7a2a,#c23a2a 60%,#f0e6d0)}
.pic-b{background:linear-gradient(135deg,#e8d8b8,#c48a5a)}
.pic-c{background:linear-gradient(135deg,#d8b080,#6a4a2a)}
.pic-d{background:linear-gradient(135deg,#c43a2a,#e8a070 60%,#4a8a3a)}

/* contact */
.contact{left:0;top:2720px;width:1200px;height:489px;background:radial-gradient(ellipse at 80% 40%,#3a2a22 0%,#1c1a19 55%,#121212 100%)}
.contact h2{position:absolute;left:0;top:66px;width:1200px;font-size:38px;color:#fff}
.contact .lead{position:absolute;left:0;top:134px;width:1200px;text-align:center;font-size:14px;color:#fff}
.contact .lead b{color:var(--red);font-weight:600}
.field{position:absolute;left:204px;width:375px;height:38px;border:1px solid rgba(255,255,255,.6);font-size:12px;color:#bbb;padding:9px 12px}
.field.msg{left:619px;width:374px;height:164px}
.contact .btn-red{position:absolute;left:512px;top:403px;width:176px;text-align:center;font-size:16px}

/* event */
.event-head{left:0;top:3280px;width:1200px}
.event-head h2{font-size:38px}
.event-head p{text-align:center;font-size:12.5px;margin-top:22px}
.event-photo{left:158px;top:3413px;width:884px;height:346px;background:radial-gradient(ellipse at 60% 50%,#c04a2a 0%,#8a5a3a 35%,#3a4a2a 75%,#1e2a1a 100%)}
.countdown{left:253px;top:3672px;width:702px;height:87px;background:#fff;display:flex}
.cd{flex:1;text-align:center;font-family:"Montserrat",sans-serif;color:var(--ink);padding-top:10px}
.cd b{display:block;font-size:38px;font-weight:400;line-height:42px}
.cd span{font-size:17px}
.arrow{top:3573px;width:50px;height:50px;border:2px solid #ddd;border-radius:50%}
.event-date{left:0;top:3820px;width:1200px;text-align:center;font-size:22px}
.event-title{left:0;top:3862px;width:1200px;font-size:32px}
.event-copy{left:240px;top:3910px;width:720px;text-align:center;font-size:14px;line-height:22px}

/* footer */
.footer{left:0;top:4023px;width:1200px;height:294px;background:linear-gradient(180deg,#1e2a1e,#121512)}
.fcol{position:absolute;top:66px;color:#fff}
.fcol h5{font-family:"Montserrat",sans-serif;font-size:15px;font-weight:500;margin-bottom:20px}
.fcol p{font-size:11.5px;line-height:17px;width:215px;color:#ccc}
.fcol ul{list-style:none}
.fcol li{font-size:12.5px;color:#ddd;margin-bottom:10px;padding-left:20px;position:relative}
.fcol li::before{content:"";position:absolute;left:2px;top:5px;width:6px;height:6px;border-top:1.5px solid #ccc;border-right:1.5px solid #ccc;transform:rotate(45deg)}
.subscribe{display:flex;width:234px;height:38px}
.subscribe div{flex:1;background:#fff;font-size:11px;color:#999;padding:11px 12px}
.subscribe span{width:44px;background:var(--red);display:flex;align-items:center;justify-content:center}
.copyright{position:absolute;left:0;bottom:12px;width:1200px;text-align:center;font-size:11px;color:#aaa}
</style>
</head>
<body>

<!-- Hero -->
<div class="abs hero" role="img" aria-label="Dark wooden table with pans, spices and fresh tomatoes"></div>
<div class="abs hero-shade"></div>
<div class="abs brand"><span class="brand-dot"></span>Brookmere Cafe</div>
<div class="abs topbar">
  <span class="social"></span><span class="social"></span><span class="social"></span><span class="social"></span><span class="social"></span>
  <span class="cart">Your Cart</span><span class="cart">0 Items - £0.00</span>
</div>
<nav class="abs nav"><span>HOME</span><span>ABOUT US</span><span>MENU</span><span>EVENT</span><span>MARKET</span><span>EMPLOYEE</span><span>CONTACT US</span></nav>
<div class="abs hero-text">
  <div class="small">FRESH FOOD</div>
  <div class="big">RESTAURANT</div>
  <p>Lorem ipsum dolor sit amet, consectetur adipiscing elit, sed do eiusmod tempor incididunt ut labore et dolore magna aliqua. Lorem ipsum dolor sit amet, consectetur adipiscing elit.</p>
  <span class="btn-ghost">LEARN MORE</span>
</div>
<div class="abs dots"><i></i><i class="on"></i><i></i></div>

<!-- Info bar -->
<div class="abs infobar">
  <div class="info">
    <svg viewBox="0 0 44 44" fill="none" stroke="#fff" stroke-width="2.5"><circle cx="22" cy="22" r="18"/><path d="M22 11v11l7 5"/></svg>
    <div><b>Opening Hours</b><span>Mon-Fri, 8:00 AM - 9:00 PM</span></div><i class="bubble"></i>
  </div>
  <div class="info">
    <svg viewBox="0 0 44 44" fill="none" stroke="#fff" stroke-width="2.5"><path d="M5 21L22 7l17 14"/><path d="M10 17v21h24V17"/><path d="M18 38V27h8v11"/></svg>
    <div><b>Address</b><span>48 Willow Lane, Chicago</span></div><i class="bubble"></i>
  </div>
  <div class="info">
    <svg viewBox="0 0 44 44" fill="none" stroke="#fff" stroke-width="2.5"><rect x="13" y="4" width="18" height="36" rx="3"/><path d="M13 32h18M20 36h4"/></svg>
    <div><b>Phone</b><span>0800 55 1200</span></div>
  </div>
</div>

<!-- About -->
<div class="abs about-photo" role="img" aria-label="Platter of figs, eggs, olives and grapes on a dark table"></div>
<div class="abs about-panel">
  <h2 class="heading">ABOUT US</h2>
  <div class="script">The Beginnings</div>
  <p>Lorem ipsum dolor sit amet, consectetur adipiscing elit, sed do eiusmod tempor incididunt ut labore et dolore magna aliqua. Ut enim ad minim veniam, quis nostrud exercitation ullamco laboris nisi ut aliquip ex ea commodo consequat. Duis aute irure dolor in reprehenderit in voluptate velit esse cillum dolore eu fugiat nulla pariatur. Excepteur sint occaecat cupidatat non proident.</p>
  <p>Lorem ipsum dolor sit amet, consectetur adipiscing elit, sed do eiusmod tempor incididunt ut labore et dolore magna aliqua. Ut enim ad minim veniam, quis nostrud exercitation ullamco laboris nisi ut aliquip ex ea commodo consequat. Duis aute irure dolor in reprehenderit in voluptate velit esse cillum dolore eu fugiat nulla pariatur. Excepteur sint occaecat cupidatat non proident.</p>
  <span class="btn-red">LEARN MORE</span>
</div>

<!-- Gallery -->
<div class="abs gallery-title"><h2 class="heading">FOOD GALLERY</h2><div class="underline"></div></div>
<div class="abs ph g1" role="img" aria-label="Yellow dessert on a plate with green leaves"></div>
<div class="abs ph g2" role="img" aria-label="Cup of coffee on a dark counter"></div>
<div class="abs ph g3" role="img" aria-label="Grilled dish served on wooden board"></div>
<div class="abs ph g4" role="img" aria-label="Fresh vegetables and cutlery on a table"></div>
<div class="abs ph g5" role="img" aria-label="Restaurant interior with bottles on a shelf"></div>

<!-- Share -->
<div class="abs share">
  <h3>SHARE YOUR PHOTOS WITH US</h3>
  <p>Lorem ipsum dolor sit amet, consectetur adipiscing elit, sed do eiusmod tempor incididunt ut labore et dolore magna aliqua</p>
  <div class="share-btn">SHARE</div>
</div>

<!-- Menu -->
<section class="abs menu">
  <div class="menu-head">
    <h2 class="heading">OUR SPECIAL MENU</h2><div class="underline"></div>
    <p>The role of a good cook ware in the preparation of a sumptuous meal cannot be over emphasized then one consider white bread</p>
  </div>
  <div class="tabs"><span class="tab active">BREAKFAST</span><span class="tab">DESERT</span><span class="tab">DINNER</span><span class="tab">FRESHFOOD</span><span class="tab">LUNCH</span></div>

  <div class="dish" style="left:86px;top:302px"><div class="pic pic-a" role="img" aria-label="Fresh salad plate"></div><h4 class="script">Lazal Cheese</h4><span class="price">£15.00</span><p>Pellentesque habitant morbi tristique senectus et netus et malesuada fames ac. <em>More</em></p></div>
  <div class="dish" style="left:616px;top:302px"><div class="pic pic-d" role="img" aria-label="Salad with tomatoes"></div><h4 class="script">Salad Beef</h4><span class="price">£15.00</span><p>Pellentesque habitant morbi tristique senectus et netus et malesuada fames ac. <em>More</em></p></div>
  <div class="dish" style="left:86px;top:443px"><div class="pic pic-b" role="img" aria-label="Slice of cake"></div><h4 class="script">Chinese Egg Cake</h4><span class="price">£15.00</span><p>Pellentesque habitant morbi tristique senectus et netus et malesuada fames ac. <em>More</em></p></div>
  <div class="dish" style="left:616px;top:443px"><div class="pic pic-c" role="img" aria-label="Beef spaghetti dish"></div><h4 class="script">Beef Spaghetti</h4><span class="price">£15.00</span><p>Pellentesque habitant morbi tristique senectus et netus et malesuada fames ac. <em>More</em></p></div>
  <div class="dish" style="left:86px;top:590px"><div class="pic pic-d" role="img" aria-label="Dessert combo plate"></div><h4 class="script">Dessert Combo</h4><span class="price">£15.00</span><p>Pellentesque habitant morbi tristique senectus et netus et malesuada fames. <em>More</em></p></div>
  <div class="dish" style="left:616px;top:590px"><div class="pic pic-a" role="img" aria-label="Cheese salad plate"></div><h4 class="script">Lazal Cheese</h4><span class="price">£15.00</span><p>Pellentesque habitant morbi tristique senectus et netus et malesuada fames ac. <em>More</em></p></div>
</section>

<!-- Contact -->
<section class="abs contact" role="img" aria-label="Dim restaurant table with a wine glass in the background">
  <h2 class="heading">CONTACT US</h2>
  <p class="lead">We are willing to help you make the reservation online or call us directly <b>(08) 5550142</b></p>
  <div class="field" style="top:198px">Name</div>
  <div class="field" style="top:262px">Email</div>
  <div class="field" style="top:325px">Phone</div>
  <div class="field msg" style="top:198px">Message</div>
  <span class="btn-red">SUBMIT</span>
</section>

<!-- Event -->
<div class="abs event-head"><h2 class="heading">UPCOMING EVENT</h2><div class="underline"></div><p>Our board of specials evolves on a daily basis according to what is sourced at the fish market that morning</p></div>
<svg class="abs arrow" style="left:16px" viewBox="0 0 50 50"><path d="M29 16l-9 9 9 9" fill="none" stroke="#ddd" stroke-width="2"/></svg>
<svg class="abs arrow" style="left:1126px" viewBox="0 0 50 50"><path d="M21 16l9 9-9 9" fill="none" stroke="#ddd" stroke-width="2"/></svg>
<div class="abs event-photo" role="img" aria-label="Plated dinner with grilled meat and salad"></div>
<div class="abs countdown">
  <div class="cd"><b>01</b><span>DAYS</span></div>
  <div class="cd"><b>07</b><span>HOURS</span></div>
  <div class="cd"><b>37</b><span>MINUTES</span></div>
  <div class="cd"><b>48</b><span>SECONDS</span></div>
</div>
<div class="abs event-date script" style="font-weight:500">October 7, 2017</div>
<h3 class="abs event-title heading">TASTED NEW BROOKMERE CAFE</h3>
<p class="abs event-copy">At vero eos et accusamus et iusto odio dignissimos ducimus qui blanditiis praesentium voluptatum deleniti atque corrupti quos dolores et quas molestias excepturi sint occaecati cupiditate non provident.</p>

<!-- Footer -->
<footer class="abs footer" role="img" aria-label="Dark green leafy background">
  <div class="fcol" style="left:115px"><h5>About Us</h5><p>Totam rem aperiam, eaque ipsa quae ab illo inventore veritatis et quasi architecto beatae vitae dicta sunt explicabo. Nemo enim ipsam.</p></div>
  <div class="fcol" style="left:417px"><h5>Quick Links</h5><ul><li>Home</li><li>About Us</li><li>Menu</li><li>Event</li></ul></div>
  <div class="fcol" style="left:636px"><h5>Menu</h5><ul><li>Break Fast</li><li>Lunch</li><li>Dinner</li></ul></div>
  <div class="fcol" style="left:875px"><h5>Subscribe Newsletter</h5>
    <div class="subscribe"><div>Enter Your Email</div><span><svg width="18" height="14" viewBox="0 0 18 14"><rect x="1" y="1" width="16" height="12" fill="none" stroke="#fff" stroke-width="1.5"/><path d="M1 1l8 6 8-6" fill="none" stroke="#fff" stroke-width="1.5"/></svg></span></div>
  </div>
  <div class="copyright">brookmerecafe.com2017. All rights reserved.</div>
</footer>

</body>
</html>
```